RTV Photography Business Card Design

I would like a business card designed in the shape of a camera.
Would like to see various camera designs. Would like to see what the card looks like in different colors. Would like to see which logo looks better on the various camera designs so please show me some with the white logo and some with the black logo. If you need a different file formats please let me know.
Project Deadline Extended Reason: My grandfather passed away and dealing with funeral plans so need to extend deadline. Added Tuesday, March 1, 2016
Project Deadline Extended
Reason: I just got back from out of town. My grandfather's passing was the primary focus for me these past few weeks and the funeral is over so now I will concentrate on picking my business card design. I really appreciate each designer who has taken the time to submit a design. Your effort has not gone unnoticed. I look forward to seeing more amazing designs.
Industry/Entity Type
Business
Contact Information for Business Card
Wren
757-418-2096
https://www.facebook.com/rtvphotographyfreelance/
DoraWren@rtv-photography.example
Look and feel

```html
<!DOCTYPE html>
<html lang="en">
<head>
<meta charset="utf-8">
<title>RTV Photography – Camera Business Card</title>
<link href="https://fonts.googleapis.com/css2?family=Questrial&family=Cinzel:wght@500&display=swap" rel="stylesheet">
<style>
  :root {
    --backdrop: #111111;
    --card-yellow: #f3dc1c;
    --card-yellow-deep: #d9b90a;
    --card-edge: #b89a06;
    --card-black: #0b0b0b;
    --brand-gold: #d7a93e;
  }
  html, body {
    margin: 0;
    padding: 0;
    width: 1200px;
    height: 900px;
    overflow: hidden;
    background: var(--backdrop);
  }
  .canvas {
    width: 1200px;
    height: 900px;
    display: flex;
    align-items: center;
    justify-content: center;
  }
  .camera-card {
    width: 880px;
    height: auto;
    display: block;
  }
  .card-body { fill: url(#yellowSheen); stroke: var(--card-edge); stroke-width: 3; }
  .card-black { fill: var(--card-black); }
  .card-yellow { fill: var(--card-yellow); }
  .lens-ring { fill: none; stroke: var(--card-yellow); }
  .holder-name {
    font-family: "Questrial", sans-serif;
    font-size: 30px;
    letter-spacing: 1px;
    fill: var(--card-yellow);
  }
  .phone-label {
    font-family: "Questrial", sans-serif;
    font-size: 20px;
    fill: var(--card-black);
  }
  .phone-number {
    font-family: "Questrial", sans-serif;
    font-size: 44px;
    fill: var(--card-black);
  }
  .brand-name {
    font-family: "Cinzel", serif;
    font-weight: 500;
    font-size: 19px;
    letter-spacing: 0.5px;
    fill: var(--brand-gold);
  }
  .brand-dot { fill: var(--brand-gold); }
</style>
</head>
<body>
<main class="canvas">
  <svg class="camera-card" viewBox="0 0 800 520" xmlns="http://www.w3.org/2000/svg" aria-label="Camera-shaped business card for RTV Photography">
    <defs>
      <linearGradient id="yellowSheen" x1="0" y1="0" x2="1" y2="1">
        <stop offset="0" stop-color="#f7e540"/>
        <stop offset="0.6" stop-color="#f1d816"/>
        <stop offset="1" stop-color="#d9b90a"/>
      </linearGradient>
    </defs>

    <g class="card-outline">
      <rect class="card-body" x="60" y="92" width="80" height="50" rx="14"/>
      <rect class="card-body" x="180" y="36" width="260" height="120" rx="30"/>
      <rect class="card-body" x="20" y="118" width="760" height="382" rx="46"/>
      <rect x="183" y="110" width="254" height="20" fill="#f3dc1c"/>
    </g>

    <g class="top-panel">
      <rect class="card-black" x="204" y="60" width="212" height="110" rx="18"/>
      <path class="card-black" d="M70 145 H730 Q756 145 756 172 V300 H44 V172 Q44 145 70 145 Z"/>
      <path class="card-yellow" d="M44 280 Q44 262 70 262 H300 Q360 262 380 300 V478 H70 Q44 478 44 452 Z"/>
      <rect class="card-yellow" x="255" y="88" width="110" height="34" rx="17"/>
    </g>

    <g class="lens">
      <circle class="card-black" cx="565" cy="305" r="172"/>
      <circle class="lens-ring" cx="565" cy="305" r="154" stroke-width="12"/>
      <circle class="lens-ring" cx="580" cy="302" r="128" stroke-width="4"/>
    </g>

    <g class="brand">
      <circle class="brand-dot" cx="580" cy="266" r="22"/>
      <text class="brand-name" x="580" y="326" text-anchor="middle">RTV PHOTOGRAPHY</text>
    </g>

    <text class="holder-name" x="74" y="226">DORA WREN</text>
    <text class="phone-label" x="74" y="392">PHONE</text>
    <text class="phone-number" x="72" y="440">555-1234</text>
  </svg>
</main>
</body>
</html>
```